Business card for Cat Cafe

I have started a small business and need a business card designed. The business is a cat cafe, that is, an ordinary cafe that serves coffee and snacks but with a twist - you can bring your cat to play. In fact the idea is to encourage everyone to come and bring your feline friend in order to build community and provide some fun and connections between fellow cat lovers. Themes of the business include;

- Fun
- Discovery
- Connections

The name of the cafe is Brews and Whiskers!

We look forward to seeing what creative ideas you may have!
Updates

Hi,

 Please note the contact details as below;
14 Tarrant Lane, Marlow Vale,
Sydney, NSW
2010

Target Market(s)

Cat owners, any age group

Industry/Entity Type

Small Business

Requirements
Must have
• Must include some type of imagery of a cat itself.

```html
<!DOCTYPE html>
<html lang="en">
<head>
<meta charset="utf-8">
<title>Brews and Whiskers! – Business Card</title>
<link rel="stylesheet" href="https://fonts.googleapis.com/css2?family=Open+Sans:wght@400;600&display=swap">
<style>
  :root {
    --backdrop: #2b2b2b;
    --cream: #f3efe7;
    --cream-deep: #e6d9c4;
    --bean-tone: #d8bf9c;
    --tan: #b88a5c;
    --tan-light: #c99c6d;
    --tan-dark: #a47849;
    --ink: #141414;
    --sticker: #ffffff;
    --brand-brown: #a57a4c;
    --white: #ffffff;
  }
  * { box-sizing: border-box; margin: 0; padding: 0; }
  html, body { width: 1200px; height: 1000px; overflow: hidden; }
  body {
    background: var(--backdrop);
    font-family: "Open Sans", Arial, sans-serif;
  }
  .card {
    position: absolute;
    left: 350px;
    top: 113px;
    width: 500px;
    height: 774px;
    border-radius: 28px;
    overflow: hidden;
    background: linear-gradient(180deg, var(--tan-light), var(--tan) 55%, var(--tan-dark));
  }
  .bean-pattern {
    position: absolute;
    left: 0; top: 0;
    width: 100%;
    height: 340px;
    background: radial-gradient(circle at 30% 30%, var(--cream) 0%, var(--cream-deep) 70%, var(--bean-tone) 130%);
  }
  .divider-band {
    position: absolute;
    left: 0; top: 326px;
    width: 190px;
    height: 22px;
    background: var(--ink);
  }
  .logo-sticker {
    position: absolute;
    left: 168px;
    top: 150px;
    width: 312px;
    height: 200px;
    border-radius: 26px;
    background: var(--sticker);
    box-shadow: 0 6px 14px rgba(0,0,0,.18);
    padding: 34px 26px 0;
  }
  .brand-name {
    font-weight: 600;
    font-size: 40px;
    line-height: 1.05;
    color: var(--brand-brown);
  }
  .brand-tagline {
    margin-top: 14px;
    font-size: 24px;
    font-weight: 400;
    color: var(--brand-brown);
  }
  .cat-illustration {
    position: absolute;
    left: 0;
    top: 400px;
    width: 230px;
    height: 374px;
    border-top-right-radius: 120px;
    background: linear-gradient(180deg, #222, var(--ink));
  }
  .themes {
    position: absolute;
    left: 252px;
    top: 470px;
    color: var(--white);
    font-size: 36px;
    font-weight: 600;
    line-height: 1.22;
  }
  .social {
    position: absolute;
    left: 28px;
    top: 700px;
    display: flex;
    align-items: center;
    gap: 12px;
    color: var(--white);
    font-size: 19px;
    font-weight: 400;
  }
  .social-dot {
    width: 30px; height: 30px;
    border-radius: 50%;
    background: var(--white);
  }
</style>
</head>
<body>
  <div class="card">
    <div class="bean-pattern" role="img" aria-label="Repeating coffee bean outline pattern on cream"></div>
    <div class="divider-band"></div>

    <div class="cat-illustration" role="img" aria-label="Stylised black cat illustration sitting with a curling tail"></div>

    <div class="logo-sticker">
      <p class="brand-name">Brews and Whiskers!</p>
      <p class="brand-tagline">Coffee and Snacks</p>
    </div>

    <div class="themes">
      <p>Fun</p>
      <p>Discovery</p>
      <p>Connections</p>
    </div>

    <div class="social">
      <span class="social-dot"></span>
      <span class="social-handle">BrewsandWhiskers</span>
    </div>
  </div>
</body>
</html>
```